Etiketten-Design für Honiggläser von Frühlings- & Sommerhonig gesucht
Wie sagte mein Sohn nach seinem Knuddelreferat in der ersten Klasse? "Gut gelaufen!"
Zielgruppe
Wir sind eine kleine Imkerei und wir suchen ein Etikett für unsere Honiggläser. Wir wollen regional Honig verkaufen und dies betonen. Dabei wollen wir zwischen Frühlings- und Sommerhonig unterscheiden.
Name der Imkerei: Imkerei Brandt
Aufgabenstellung
Die Vorgaben finden sich auf der hochgeladenen Datei.
Eigentlich habe ich noch keine Gläser, aber sehr gut denkbar wäre das 500g-Glas von Vitrel. Das ist schick und das gibt es ohne PVC im Deckel. Die Etikettenmaße sind nicht vorgeschrieben, ich denke 8 mal 5 für die Vorderseite, 6 mal 5 für die Rückseite und 3 cm Durchmesser für den Deckel erscheinen mir sinnvoll, Änderungen der Maße sind aber auch gut möglich.
Viel Spaß und viel Erfolg beim Erstellen!

```html
<!DOCTYPE html>
<html lang="de">
<head>
<meta charset="utf-8">
<title>Honigetiketten – Imkerei Brandt</title>
<link href="https://fonts.googleapis.com/css2?family=Josefin+Sans:wght@600;700&display=swap" rel="stylesheet">
<style>
  :root {
    --page-bg: #f3efe8;
    --meadow-dark: #3f8a1e;
    --meadow-mid: #6cbf2c;
    --meadow-light: #9ad449;
    --frame-line: #f4f6d2;
    --oval-spring: #eef0c2;
    --oval-summer: #fdf0b4;
    --ink: #1c1a16;
    --bee-body: #f0a21c;
    --sprig: #2b2a24;
  }
  * { box-sizing: border-box; margin: 0; padding: 0; }
  html, body { width: 1200px; height: 852px; overflow: hidden; }
  body {
    background: var(--page-bg);
    font-family: "Josefin Sans", sans-serif;
    color: var(--ink);
    display: flex;
    align-items: center;
    justify-content: center;
    gap: 40px;
  }
  .label {
    position: relative;
    width: 540px;
    height: 336px;
    overflow: hidden;
    box-shadow: 0 4px 14px rgba(0,0,0,0.12);
  }
  .meadow-photo {
    position: absolute; inset: 0;
    background:
      radial-gradient(circle at 12% 30%, rgba(90,100,220,0.55) 0 18px, transparent 34px),
      radial-gradient(circle at 8% 75%, rgba(90,100,220,0.5) 0 20px, transparent 38px),
      radial-gradient(circle at 88% 22%, rgba(130,50,120,0.5) 0 16px, transparent 30px),
      radial-gradient(circle at 24% 88%, rgba(255,200,20,0.7) 0 18px, transparent 34px),
      radial-gradient(circle at 94% 82%, rgba(230,190,20,0.7) 0 16px, transparent 30px),
      linear-gradient(160deg, var(--meadow-light), var(--meadow-mid) 45%, var(--meadow-dark));
  }
  .label-frame { position: absolute; inset: 0; }
  .oval-badge { position: absolute; left: 0; top: 0; width: 540px; height: 336px; }
  .badge-content {
    position: absolute;
    left: 0; right: 0;
    top: 40px;
    display: flex; flex-direction: column; align-items: center;
    text-align: center;
  }
  .bee-mascot {
    width: 30px; height: 32px;
    border-radius: 50%;
    background: radial-gradient(circle at 50% 35%, var(--bee-body) 0 55%, #5a3a10 56% 70%, #f7d9a0 71%);
  }
  .brand-row {
    display: flex; align-items: center; gap: 12px;
    margin-top: 10px;
  }
  .sprig {
    width: 30px; height: 20px;
    border-radius: 50% 50% 40% 40%;
    background: radial-gradient(ellipse at 50% 40%, var(--sprig) 0 30%, transparent 60%);
    opacity: 0.8;
  }
  .brand-name {
    font-size: 17px; font-weight: 600; letter-spacing: 0.5px;
    padding-top: 3px;
  }
  .honey-title {
    margin-top: 22px;
    font-size: 30px; font-weight: 700; line-height: 1.12; letter-spacing: 0.6px;
  }
  .origin-note {
    margin-top: 24px;
    font-size: 14px; font-weight: 600; letter-spacing: 0.4px;
  }
  .net-weight {
    margin-top: 10px;
    font-size: 22px; font-weight: 700;
  }
</style>
</head>
<body>

  <article class="label label--spring">
    <div class="meadow-photo" role="img" aria-label="Foto einer bunten Blumenwiese mit Kornblumen und Mohn"></div>
    <svg class="label-frame" viewBox="0 0 540 336" aria-hidden="true">
      <rect x="10" y="10" width="520" height="316" fill="none" stroke="var(--frame-line)" stroke-width="2" stroke-dasharray="8 4"/>
      <rect x="16" y="16" width="508" height="304" fill="none" stroke="var(--frame-line)" stroke-width="1.2" stroke-dasharray="4 3"/>
    </svg>
    <svg class="oval-badge" viewBox="0 0 540 336" aria-hidden="true">
      <ellipse cx="270" cy="182" rx="188" ry="140" fill="var(--oval-spring)" stroke="var(--oval-spring)" stroke-width="6" stroke-dasharray="3 3"/>
      <ellipse cx="270" cy="182" rx="178" ry="130" fill="none" stroke="var(--ink)" stroke-width="1.4" stroke-dasharray="5 4"/>
    </svg>
    <div class="badge-content">
      <div class="bee-mascot" role="img" aria-label="Gezeichnete Biene als Maskottchen"></div>
      <div class="brand-row">
        <span class="sprig" role="img" aria-label="Blumenornament"></span>
        <span class="brand-name">IMKEREI BRANDT</span>
        <span class="sprig" role="img" aria-label="Blumenornament"></span>
      </div>
      <h2 class="honey-title">FRÄNKISCHER<br>FRÜHLINGSHONIG</h2>
      <p class="origin-note">PRODUKT AUS FRANKEN</p>
      <p class="net-weight">500g</p>
    </div>
  </article>

  <article class="label label--summer">
    <div class="meadow-photo" role="img" aria-label="Foto einer bunten Blumenwiese mit Kornblumen und Mohn"></div>
    <svg class="label-frame" viewBox="0 0 540 336" aria-hidden="true">
      <rect x="10" y="10" width="520" height="316" fill="none" stroke="var(--frame-line)" stroke-width="2" stroke-dasharray="8 4"/>
      <rect x="16" y="16" width="508" height="304" fill="none" stroke="var(--frame-line)" stroke-width="1.2" stroke-dasharray="4 3"/>
    </svg>
    <svg class="oval-badge" viewBox="0 0 540 336" aria-hidden="true">
      <ellipse cx="270" cy="182" rx="188" ry="140" fill="var(--oval-summer)" stroke="var(--oval-summer)" stroke-width="6" stroke-dasharray="3 3"/>
      <ellipse cx="270" cy="182" rx="178" ry="130" fill="none" stroke="var(--ink)" stroke-width="1.4" stroke-dasharray="5 4"/>
    </svg>
    <div class="badge-content">
      <div class="bee-mascot" role="img" aria-label="Gezeichnete Biene als Maskottchen"></div>
      <div class="brand-row">
        <span class="sprig" role="img" aria-label="Blumenornament"></span>
        <span class="brand-name">IMKEREI BRANDT</span>
        <span class="sprig" role="img" aria-label="Blumenornament"></span>
      </div>
      <h2 class="honey-title">FRÄNKISCHER<br>SOMMERHONIG</h2>
      <p class="origin-note">PRODUKT AUS FRANKEN</p>
      <p class="net-weight">500g</p>
    </div>
  </article>

</body>
</html>
```